Website for Apartment Rental in Prague

I would like to create designs of my website focused on luxury apartment rentals in Prague, Czech Republic. I created initial mock-ups, They are all attached. I need to design homepage and subpage. The mock-ups were created by combining elements from different websites that I liked but I need you to create a design that is unique and original. The attached files a only a guidance for the structure of the website but not for the design. Try to be creative.

Industry/Entity Type

Apartment

```html
<!DOCTYPE html>
<html lang="en">
<head>
<meta charset="utf-8">
<title>Vltava Residences — Home</title>
<link href="https://fonts.googleapis.com/css2?family=Montserrat:wght@400;500;600;700;800&display=swap" rel="stylesheet">
<style>
:root{
  --accent:#e8d63c;
  --brand-brown:#9c7f6e;
  --nav-bg:#4b5649;
  --text-dark:#3e3e3e;
  --text-mid:#6b6b6b;
  --text-soft:#9a9a9a;
  --line:#e3e3e3;
  --card-foot:#f3f3f3;
  --sale:#e86a5d;
  --rent:#5fb45a;
  --white:#ffffff;
}
*{box-sizing:border-box;margin:0;padding:0}
html,body{width:1200px;height:950px;overflow:hidden;background:var(--white);font-family:'Montserrat',sans-serif;color:var(--text-dark)}
.page{position:relative;width:1200px;height:950px;overflow:hidden}

/* header */
.topbar{position:absolute;left:0;top:0;width:1200px;height:56px;background:#f7f7f5;border-top:2px solid var(--accent)}
.brand{position:absolute;left:232px;top:14px;display:flex;align-items:center;gap:8px}
.brand-mark{width:24px;height:24px;border:3px solid var(--brand-brown)}
.brand-name{font-size:12px;font-weight:700;color:var(--brand-brown);line-height:12px;letter-spacing:.3px;text-transform:uppercase;width:100px}
.contact{position:absolute;left:694px;top:14px;display:flex;gap:6px}
.contact svg{margin-top:3px}
.contact .phone{font-size:15px;color:#555;font-weight:400;line-height:16px}
.contact .mail{font-size:8px;color:var(--text-soft);margin-top:1px}
.contact-divider{position:absolute;left:820px;top:18px;width:1px;height:20px;background:#ddd}
.dropdown{position:absolute;top:18px;height:19px;border:1px solid #ddd;background:#fff;font-size:7.5px;color:#555;display:flex;align-items:center;padding:0 6px;gap:5px}
.dropdown.currency{left:838px;width:47px}
.dropdown.lang{left:903px;width:63px}
.flag{width:10px;height:7px;background:#4a5a9a;border:1px solid #c44}

/* navigation */
.nav{position:absolute;left:0;top:56px;width:1200px;height:38px;background:var(--nav-bg);z-index:3}
.nav ul{list-style:none;position:absolute;left:234px;top:0;height:38px;display:flex;align-items:center}
.nav li{font-size:8px;font-weight:600;color:var(--white);letter-spacing:.3px;display:flex;align-items:center}
.nav li.active{color:var(--accent)}
.nav li .sep{color:#9aa397;margin:0 13px}
.nav li .caret{margin-left:3px;font-size:7px}
.nav-search{position:absolute;left:928px;top:0;width:38px;height:38px;background:var(--brand-brown);display:flex;align-items:center;justify-content:center}

/* hero */
.hero{position:absolute;left:0;top:94px;width:1200px;height:482px;background:linear-gradient(180deg,#8a8a86 0%,#6e5540 22%,#5a3e2c 45%,#41443e 60%,#2d5560 75%,#1f4a55 100%)}
.hero-caption{position:absolute;left:0;top:148px;width:1200px;height:114px;background:rgba(40,40,40,.35);text-align:center;color:var(--white)}
.hero-title{font-size:24px;font-weight:800;margin-top:16px;letter-spacing:.5px}
.hero-rule{width:18px;height:2px;background:var(--accent);margin:6px auto 0}
.hero-loc{font-size:8px;font-weight:500;margin-top:10px;display:flex;justify-content:center;align-items:center;gap:5px}
.hero-price{font-size:15px;font-weight:700;color:var(--accent);margin-top:14px;letter-spacing:.5px}
.hero-arrow{position:absolute;top:186px}

.search-tabs{position:absolute;left:234px;top:384px;display:flex;gap:2px}
.tab{height:26px;padding:0 9px;font-size:8px;font-weight:600;color:var(--white);background:rgba(40,50,45,.75);display:flex;align-items:center}
.tab.active{background:rgba(40,50,45,.95)}
.adv-tab{position:absolute;left:870px;top:384px;width:96px;height:26px;background:rgba(40,50,45,.9);color:var(--white);font-size:8px;font-weight:600;display:flex;align-items:center;justify-content:center}
.search-bar{position:absolute;left:0;top:410px;width:1200px;height:72px;background:rgba(25,45,45,.55);border-bottom:2px solid #6ea0c8}
.field{position:absolute;top:16px}
.field label{display:block;font-size:8px;font-weight:500;color:var(--white);margin-bottom:3px}
.select{height:25px;background:var(--white);font-size:8px;color:var(--text-soft);display:flex;align-items:center;justify-content:space-between;padding:0 6px 0 8px}
.select .box{width:9px;height:9px;background:#8a8a8a;display:flex;align-items:center;justify-content:center}
.price{position:absolute;left:672px;top:28px;width:169px;color:var(--white)}
.price-row{display:flex;justify-content:space-between;font-size:8px;font-weight:600}
.price-row .label{font-weight:500}
.track{position:relative;margin-top:8px;height:3px;background:#d5d5d5}
.track .fill{position:absolute;left:8px;width:133px;top:0;height:3px;background:var(--white)}
.track .knob{position:absolute;top:-2px;width:7px;height:7px;border-radius:50%;background:var(--accent)}
.search-btn{position:absolute;left:859px;top:21px;width:107px;height:25px;background:var(--accent);color:var(--white);font-size:8px;font-weight:700;display:flex;align-items:center;justify-content:center;letter-spacing:.5px}

/* featured */
.section-head{position:absolute;left:234px;top:612px;width:732px;height:30px;display:flex;align-items:center}
.section-head .rule{flex:1;height:3px;border-top:1px solid var(--line);border-bottom:1px solid var(--line)}
.section-head .title{display:flex;align-items:center;gap:12px;margin:0 14px 0 18px}
.section-head h2{font-size:22px;font-weight:500;color:#555;letter-spacing:1.5px}
.sq-arrow{width:12px;height:12px;background:var(--brand-brown);display:flex;align-items:center;justify-content:center}

.card{position:absolute;top:654px;width:232px;height:206px;background:var(--white);border:1px solid #ececec}
.card.ghost{opacity:.22}
.card-media{position:relative;height:128px}
.card-media .badge{position:absolute;left:0;top:6px;font-size:10px;font-weight:600;color:var(--white);padding:1px 4px}
.badge.sale{background:var(--sale)}
.badge.rent{background:var(--rent)}
.card-media .tag-price{position:absolute;right:0;top:6px;font-size:10px;font-weight:500;color:var(--white);background:var(--sale);padding:1px 4px}
.card-media .name{position:absolute;left:0;bottom:0;width:100%;height:30px;background:linear-gradient(180deg,rgba(0,0,0,0),rgba(0,0,0,.55));color:var(--white);font-size:11.5px;font-weight:700;padding:8px 11px 0}
.specs{display:grid;grid-template-columns:113px 1fr;row-gap:6px;padding:10px 12px 0;height:50px;font-size:7.5px;color:var(--text-mid)}
.specs span{display:flex;align-items:center;gap:5px}
.specs b{font-weight:500;color:var(--text-dark)}
.card-foot{position:absolute;left:0;bottom:0;width:100%;height:28px;background:var(--card-foot);font-size:7.5px;color:var(--text-mid);display:flex;align-items:center;gap:5px;padding-left:12px}
.card.selected .card-foot{border-bottom:2px solid var(--brand-brown)}
.card.selected .card-media{background:#b09382}
.fade-left{position:absolute;left:0;top:650px;width:240px;height:215px;background:linear-gradient(90deg,#fff 0%,rgba(255,255,255,0) 100%)}
.fade-right{position:absolute;left:960px;top:650px;width:240px;height:215px;background:linear-gradient(270deg,#fff 0%,rgba(255,255,255,0) 100%)}

.all-btn{position:absolute;left:547px;top:884px;width:106px;height:25px;background:#f5efb8;border:1px solid #ece4a0;color:#c9b830;font-size:7.5px;font-weight:600;letter-spacing:.5px;display:flex;align-items:center;justify-content:center}
</style>
</head>
<body>
<div class="page">

  <header class="topbar">
    <div class="brand">
      <div class="brand-mark"></div>
      <div class="brand-name">Vltava Residences</div>
    </div>
    <div class="contact">
      <svg width="10" height="10" viewBox="0 0 24 24"><path fill="#9c7f6e" d="M6.6 10.8a15 15 0 0 0 6.6 6.6l2.2-2.2c.3-.3.7-.4 1-.2 1.1.4 2.3.6 3.6.6.6 0 1 .4 1 1V20c0 .6-.4 1-1 1A17 17 0 0 1 3 4c0-.6.4-1 1-1h3.5c.6 0 1 .4 1 1 0 1.3.2 2.5.6 3.6.1.3 0 .7-.2 1z"/></svg>
      <div>
        <div class="phone">123-555-0190</div>
        <div class="mail">stay@vltavaresidences.com</div>
      </div>
    </div>
    <div class="contact-divider"></div>
    <div class="dropdown currency">$ USD <span>&#709;</span></div>
    <div class="dropdown lang"><span class="flag"></span>English <span>&#709;</span></div>
  </header>

  <nav class="nav">
    <ul>
      <li class="active">HOME<span class="sep">-</span></li>
      <li>ABOUT US<span class="sep">-</span></li>
      <li>APARTMENTS<span class="caret">&#709;</span><span class="sep">-</span></li>
      <li>SERVICES<span class="caret">&#709;</span><span class="sep">-</span></li>
      <li>AGENTS<span class="caret">&#709;</span><span class="sep">-</span></li>
      <li>NEWS<span class="sep">-</span></li>
      <li>GALLERY<span class="sep">-</span></li>
      <li>CONTACT US</li>
    </ul>
    <div class="nav-search">
      <svg width="11" height="11" viewBox="0 0 24 24"><circle cx="10" cy="10" r="6.5" fill="none" stroke="#fff" stroke-width="3"/><path d="M15 15l6 6" stroke="#fff" stroke-width="3"/></svg>
    </div>
  </nav>

  <section class="hero" role="img" aria-label="Photo of a wooden mountain house at dusk with lit windows, patio umbrellas and a pool in front">
    <div class="hero-caption">
      <h1 class="hero-title">Beautiful house in Prague</h1>
      <div class="hero-rule"></div>
      <div class="hero-loc">
        <svg width="6" height="8" viewBox="0 0 12 16"><path fill="#fff" d="M6 0a6 6 0 0 0-6 6c0 4.5 6 10 6 10s6-5.5 6-10a6 6 0 0 0-6-6zm0 8.5A2.5 2.5 0 1 1 6 3.5a2.5 2.5 0 0 1 0 5z"/></svg>
        Main Street, Prague
      </div>
      <div class="hero-price">$ 125,000</div>
    </div>
    <svg class="hero-arrow" style="left:20px" width="16" height="32" viewBox="0 0 16 32"><path d="M15 1L1 16l14 15" fill="none" stroke="#fff" stroke-width="1.2"/></svg>
    <svg class="hero-arrow" style="left:1165px" width="16" height="32" viewBox="0 0 16 32"><path d="M1 1l14 15L1 31" fill="none" stroke="#fff" stroke-width="1.2"/></svg>

    <div class="search-tabs">
      <div class="tab">SALE</div>
      <div class="tab active">RENT</div>
    </div>
    <div class="adv-tab">ADVANCED SEARCH</div>

    <form class="search-bar">
      <div class="field" style="left:234px;width:106px"><label>Location</label><div class="select">All city<span class="box"><svg width="5" height="4" viewBox="0 0 10 6"><path d="M1 1l4 4 4-4" stroke="#fff" fill="none" stroke-width="1.6"/></svg></span></div></div>
      <div class="field" style="left:359px;width:107px"><label>Property type</label><div class="select">Al type<span class="box"><svg width="5" height="4" viewBox="0 0 10 6"><path d="M1 1l4 4 4-4" stroke="#fff" fill="none" stroke-width="1.6"/></svg></span></div></div>
      <div class="field" style="left:484px;width:75px"><label>Rooms</label><div class="select">Choose<span class="box"><svg width="5" height="4" viewBox="0 0 10 6"><path d="M1 1l4 4 4-4" stroke="#fff" fill="none" stroke-width="1.6"/></svg></span></div></div>
      <div class="field" style="left:578px;width:75px"><label>Bathrooms</label><div class="select">Choose<span class="box"><svg width="5" height="4" viewBox="0 0 10 6"><path d="M1 1l4 4 4-4" stroke="#fff" fill="none" stroke-width="1.6"/></svg></span></div></div>
      <div class="price">
        <div class="price-row"><span class="label">Price Range:</span><span>$ 10,000 &nbsp;&nbsp;- &nbsp;&nbsp;$ 100,000</span></div>
        <div class="track"><div class="fill"></div><div class="knob" style="left:6px"></div><div class="knob" style="left:139px"></div></div>
      </div>
      <div class="search-btn">SEARCH</div>
    </form>
  </section>

  <div class="section-head">
    <div class="rule"></div>
    <div class="title">
      <span class="sq-arrow"><svg width="5" height="7" viewBox="0 0 6 10"><path d="M5 1L1 5l4 4" stroke="#fff" fill="none" stroke-width="1.6"/></svg></span>
      <h2>FEATURED</h2>
      <span class="sq-arrow"><svg width="5" height="7" viewBox="0 0 6 10"><path d="M1 1l4 4-4 4" stroke="#fff" fill="none" stroke-width="1.6"/></svg></span>
    </div>
    <div class="rule"></div>
  </div>

  <!-- listing cards -->
  <article class="card ghost" style="left:-16px">
    <div class="card-media" role="img" aria-label="Photo of a house with scenic surroundings" style="background:#9a9a9a">
      <span class="tag-price">$ 125,000</span>
      <div class="name">with Beautiful Scenery</div>
    </div>
    <div class="specs"><span>Bedrooms: <b>4</b></span><span>Area: <b>2,450 sq.ft.</b></span><span>Bathrooms: <b>2</b></span><span>Type: <b>Villa</b></span></div>
    <div class="card-foot">Linden Lane, Oakfield, MI 48000</div>
  </article>

  <article class="card selected" style="left:234px">
    <div class="card-media" role="img" aria-label="Photo of a bright apartment kitchen interior">
      <span class="badge sale" style="background:#a88a78">SALE</span>
      <span class="tag-price" style="background:#a88a78">$ 125,000</span>
      <div class="name">Beautiful Apartment</div>
    </div>
    <div class="specs">
      <span><svg width="9" height="6" viewBox="0 0 18 12"><path fill="#aaa" d="M0 0h2v7h16v5h-2v-2H2v2H0zM4 3h5v3H4zM10 3h7v3h-7z"/></svg>Bedrooms: <b>4</b></span>
      <span><svg width="7" height="7" viewBox="0 0 10 10"><path d="M1 9l8-8M5 1h4v4M1 5v4h4" stroke="#aaa" fill="none"/></svg>Area: <b>2,450 sq.ft.</b></span>
      <span><svg width="9" height="7" viewBox="0 0 18 12"><path fill="#aaa" d="M0 5h18v2c0 3-2 5-5 5H5c-3 0-5-2-5-5zM2 0h3v5H2z"/></svg>Bathrooms: <b>2</b></span>
      <span><svg width="9" height="7" viewBox="0 0 18 12"><path fill="#aaa" d="M0 2h18v10H0zM2 4v6h2V4zm4 0v6h2V4zm4 0v6h2V4zm4 0v6h2V4z"/></svg>Type: <b>Apartment</b></span>
    </div>
    <div class="card-foot"><svg width="6" height="8" viewBox="0 0 12 16"><path fill="#aaa" d="M6 0a6 6 0 0 0-6 6c0 4.5 6 10 6 10s6-5.5 6-10a6 6 0 0 0-6-6zm0 8.5A2.5 2.5 0 1 1 6 3.5a2.5 2.5 0 0 1 0 5z"/></svg>Main Street, Prague</div>
  </article>

  <article class="card" style="left:484px">
    <div class="card-media" role="img" aria-label="Photo of a two-storey brick family house with a green lawn" style="background:linear-gradient(180deg,#c8d6e2 0%,#a8967a 45%,#6d7a4a 100%)">
      <span class="badge rent">RENT</span>
      <span class="tag-price" style="background:var(--rent)">$ 680</span>
      <div class="name">Beautiful House</div>
    </div>
    <div class="specs">
      <span><svg width="9" height="6" viewBox="0 0 18 12"><path fill="#aaa" d="M0 0h2v7h16v5h-2v-2H2v2H0zM4 3h5v3H4zM10 3h7v3h-7z"/></svg>Bedrooms: <b>3</b></span>
      <span><svg width="7" height="7" viewBox="0 0 10 10"><path d="M1 9l8-8M5 1h4v4M1 5v4h4" stroke="#aaa" fill="none"/></svg>Area: <b>1,980</b></span>
      <span><svg width="9" height="7" viewBox="0 0 18 12"><path fill="#aaa" d="M0 5h18v2c0 3-2 5-5 5H5c-3 0-5-2-5-5zM2 0h3v5H2z"/></svg>Bathrooms: <b>1</b></span>
      <span><svg width="9" height="7" viewBox="0 0 18 12"><path fill="#aaa" d="M0 2h18v10H0zM2 4v6h2V4zm4 0v6h2V4zm4 0v6h2V4zm4 0v6h2V4z"/></svg>Type: <b>House</b></span>
    </div>
    <div class="card-foot"><svg width="6" height="8" viewBox="0 0 12 16"><path fill="#aaa" d="M6 0a6 6 0 0 0-6 6c0 4.5 6 10 6 10s6-5.5 6-10a6 6 0 0 0-6-6zm0 8.5A2.5 2.5 0 1 1 6 3.5a2.5 2.5 0 0 1 0 5z"/></svg>Main Street, Prague</div>
  </article>

  <article class="card" style="left:734px">
    <div class="card-media" role="img" aria-label="Photo of a white stucco house with a red tile roof" style="background:linear-gradient(180deg,#8fb3d8 0%,#e8e4dc 40%,#c9bfb0 75%,#5c4a3a 100%)">
      <span class="badge sale">SALE</span>
      <span class="tag-price">$ 750,000</span>
      <div class="name">Beautiful Apartment</div>
    </div>
    <div class="specs">
      <span><svg width="9" height="6" viewBox="0 0 18 12"><path fill="#aaa" d="M0 0h2v7h16v5h-2v-2H2v2H0zM4 3h5v3H4zM10 3h7v3h-7z"/></svg>Bedrooms: <b>11</b></span>
      <span><svg width="7" height="7" viewBox="0 0 10 10"><path d="M1 9l8-8M5 1h4v4M1 5v4h4" stroke="#aaa" fill="none"/></svg>Area: <b>5,200</b></span>
      <span><svg width="9" height="7" viewBox="0 0 18 12"><path fill="#aaa" d="M0 5h18v2c0 3-2 5-5 5H5c-3 0-5-2-5-5zM2 0h3v5H2z"/></svg>Bathrooms: <b>4</b></span>
      <span><svg width="9" height="7" viewBox="0 0 18 12"><path fill="#aaa" d="M0 2h18v10H0zM2 4v6h2V4zm4 0v6h2V4zm4 0v6h2V4zm4 0v6h2V4z"/></svg>Type: <b>Apartment</b></span>
    </div>
    <div class="card-foot"><svg width="6" height="8" viewBox="0 0 12 16"><path fill="#aaa" d="M6 0a6 6 0 0 0-6 6c0 4.5 6 10 6 10s6-5.5 6-10a6 6 0 0 0-6-6zm0 8.5A2.5 2.5 0 1 1 6 3.5a2.5 2.5 0 0 1 0 5z"/></svg>Main Street, Prague</div>
  </article>

  <article class="card ghost" style="left:984px">
    <div class="card-media" role="img" aria-label="Photo of an apartment building" style="background:#a0a0a0">
      <span class="badge sale">SALE</span>
      <div class="name">Beautiful Apartment</div>
    </div>
    <div class="specs"><span>Bedrooms: <b>11</b></span><span>Area: <b>5,200</b></span><span>Bathrooms: <b>4</b></span><span>Type: <b>Villa</b></span></div>
    <div class="card-foot">Main Street, Prague</div>
  </article>

  <div class="fade-left"></div>
  <div class="fade-right"></div>

  <a class="all-btn">ALL LISTINGS</a>
</div>
</body>
</html>
```